Speisekarte Heuriger
Zielgruppe
Wir sind ein Gastronomielokal im Burgenland. Ein Heuriger ist ein traditionelles Lokal in dem hauptsächlich kalte und einfache warme Speisen verabreicht werden. (Brote, kaltes und warmes gebratenes Fleisch, gemischte Teller, Strudl usw.) Aber ein großer Schwerpunkt liegt dabei auch immer auf den eigenen Weinen.
Aufgabenstellung
Da ein Heuriger aus dem Weinbau und somit Landwirtschaft kommt bevorzuge ich eher ein schlichtes traditionelles Design. Ein grüner Farbbereich ist vielleicht das Beste. (nicht stechend grün. eher hell) (Vielleicht im Internet nach Speisekarte Heuriger/Buschenschank suchen)
Ich benötige eine Vorlage für die Speisekarte in Indesign am besten erstellt mit dem drukwelle.at plugin damit die Größen passen.
Speisekarte mit Umschlag 8 Innenseiten mit 4seitigem Umschlag haben.
In A5 hoch
CMYK-Farbmodell
Klammerheftung
Umschlag:
Vorderseite natürlich mit "Speisekarte" drauf mit Logo, Und evtl der Name: "Heuriger Familie Pelkinger" usw.
die vordere Innenseite kann leer sein. Evtl auch gesamte Anschrift hier rein. Oder auch auf die Rückseite. Das ist freigestellt.
Auf der hinteren Innenseite muss die Allergenverordnung mit den Allergenen und dazugehörigen Buchstaben vorhanden sein! (Achtung für Österreich! Gibt genug Beispielbilder im Internet)
Auf der Rückseite hinten sollte stehen: "Wir bedanken uns für Ihren Besuch und freuen uns darauf, Sie bald wieder bei uns begrüßen zu dürfen!
Familie Pelkinger" (Natürlich nicht in einer Wurst)
Innenseiten: (Text schreibe ich selber. Aber vielleicht ein paar Beispiele für Schriftart und Größe/Farbe)
Erste Seite (rechts): Getränke
Zweite Seite: Kalte Speisen
Dritte Seite: Brote
Vierte Seite: Warme Speisen
Fünfte Seite: Beilagen/Salate
Sechste Seite: Für unsere kleinen Gäste/ Strudel
Siebente Seite: Weißwein
Achte Seite: Rotwein
Die Seitenbelegung ist nur als Info gedacht. Ich habe leider keine schönen Fotos von den Speisen gemacht und will auch keine fremden Speisen in meiner Karte sehen. Also keine Speisebilder. (Mit Ausnahme von Weintrauben vielleicht. Bezug zum Weinbau usw.)
Anbei habe ich die Logos von unseren Etiketten. Man kann das P auch alleine ohne dem Namen darunt..

```html
<!DOCTYPE html>
<html lang="de">
<head>
<meta charset="utf-8">
<title>Speisekarte – Heuriger Familie Pelkinger</title>
<link href="https://fonts.googleapis.com/css2?family=Nunito+Sans:ital,wght@0,300;0,400;0,600;1,300&display=swap" rel="stylesheet">
<style>
  :root {
    --backdrop: #2f2f2f;
    --paper: #e2e8c6;
    --paper-light: #e8edd0;
    --ink: #3d3d38;
    --ink-soft: #66665c;
    --accent: #80bb3c;
    --rule: #f6f8ee;
    --label-bg: #fbfbf6;
  }
  * { margin: 0; padding: 0; box-sizing: border-box; }
  html, body {
    width: 1200px; height: 848px; overflow: hidden;
    background: var(--backdrop);
    font-family: "Nunito Sans", sans-serif;
    color: var(--ink);
  }
  .canvas { position: relative; width: 1200px; height: 848px; }

  .page {
    position: absolute; top: 140px; height: 517px;
    background: radial-gradient(ellipse at 40% 35%, var(--paper-light), var(--paper) 75%);
  }
  .page--cover { left: 34px; width: 364px; }
  .page--cold  { left: 414px; width: 364px; }
  .page--warm  { left: 793px; width: 366px; }

  /* cover */
  .cover-info {
    position: absolute; left: 147px; top: 196px;
    font-weight: 400; color: var(--ink);
  }
  .cover-info .house {
    font-size: 8.6px; letter-spacing: 5.2px; line-height: 14.7px;
    text-transform: uppercase; margin-bottom: 11px;
  }
  .cover-info .address { font-size: 8.6px; letter-spacing: 1.6px; line-height: 14.7px; }
  .cover-info .mail { font-size: 7.6px; letter-spacing: 0.2px; line-height: 12px; }

  /* section label */
  .section-label {
    position: absolute; left: 135px; top: 0; width: 94px; height: 88px;
    background: var(--label-bg);
    display: flex; flex-direction: column; align-items: center; justify-content: flex-end;
    padding-bottom: 13px; color: var(--accent);
  }
  .page--warm .section-label { left: 136px; }
  .section-label .brand {
    font-size: 8px; font-weight: 400; letter-spacing: 1px;
    margin-bottom: 14px;
  }
  .section-label .title {
    font-size: 9px; font-weight: 600; letter-spacing: 3.6px;
    line-height: 14.5px; text-align: center; text-transform: uppercase;
    padding-left: 3.6px;
  }

  /* menu list */
  .menu { position: absolute; list-style: none; width: 224px; }
  .page--cold .menu { left: 74px; top: 134px; }
  .page--warm .menu { left: 75px; top: 182px; }
  .menu-item {
    display: grid; grid-template-columns: 136px 62px 26px;
    padding: 3px 0 4px; border-bottom: 1px solid var(--rule);
  }
  .menu-item .name {
    font-size: 8.3px; line-height: 10.5px; text-transform: uppercase; letter-spacing: 0.1px;
  }
  .menu-item .desc {
    grid-column: 1; font-size: 6.2px; line-height: 10.4px; color: var(--ink-soft); font-weight: 300;
  }
  .menu-item .allergens {
    grid-column: 2; grid-row: 1; font-size: 6.2px; font-style: italic; font-weight: 300;
    line-height: 10.5px; color: var(--ink-soft);
  }
  .menu-item .price {
    grid-column: 3; grid-row: 1; font-size: 8.3px; line-height: 10.5px; text-align: right; white-space: nowrap;
  }

  .footnote {
    position: absolute; left: 0; right: 0; top: 488px; text-align: center;
    font-size: 4.6px; font-style: italic; font-weight: 300; color: var(--ink-soft);
  }
</style>
</head>
<body>
<div class="canvas">

  <section class="page page--cover">
    <div class="cover-info">
      <p class="house">Heuriger<br>Familie<br>Pelkinger</p>
      <p class="address">Lindenweg 4<br>7051 Grünbach<br>T: 02680/4312</p>
      <p class="mail">heuriger@pelkinger.at</p>
    </div>
  </section>

  <section class="page page--cold">
    <header class="section-label">
      <span class="brand">Pelkinger</span>
      <h2 class="title">Kalte<br>Speisen</h2>
    </header>
    <ul class="menu">
      <li class="menu-item"><span class="name">Hausplatte</span><span class="allergens">A, C, H, M*</span><span class="price">€ 5,50</span><span class="desc">Sur-, Kümmelbraten, Geselchtes,<br>Presswurst und Blunze, garniert, inkl. Brot</span></li>
      <li class="menu-item"><span class="name">Luftgetrockneter<br>Rohschinken</span><span class="allergens">A, C, H, M*</span><span class="price">€ 6,00</span><span class="desc">mit Zuckermelone, garniert, inkl. Brot</span></li>
      <li class="menu-item"><span class="name">Surbraten</span><span class="allergens">A, C, H, M*</span><span class="price">€ 5,00</span><span class="desc">garniert, inkl. Brot</span></li>
      <li class="menu-item"><span class="name">Geselchtes</span><span class="allergens">A, C, H, M*</span><span class="price">€ 5,00</span><span class="desc">garniert, inkl. Brot</span></li>
      <li class="menu-item"><span class="name">Kümmelbraten</span><span class="allergens">A, C, H, M*</span><span class="price">€ 5,00</span><span class="desc">garniert, inkl. Brot</span></li>
      <li class="menu-item"><span class="name">Käseplatte</span><span class="allergens">A, C, G, H, M*</span><span class="price">€ 6,00</span><span class="desc">verschiedene Sorten Hart- und<br>Weichkäse, garniert, inkl. Brot</span></li>
      <li class="menu-item"><span class="name">Presswurst mit Zwiebel</span><span class="allergens">A, C, H, M*</span><span class="price">€ 4,00</span><span class="desc">inkl. Brot, auf Wunsch mit Kernöl</span></li>
      <li class="menu-item"><span class="name">Saure Wurst mit Zwiebel</span><span class="allergens">A, C, H, M*</span><span class="price">€ 4,00</span><span class="desc">inkl. Brot, auf Wunsch mit Kernöl</span></li>
      <li class="menu-item" style="padding:5px 0 6px"><span class="name">Käsestangerl mit Gouda</span><span class="allergens">A, C, G, H, M*</span><span class="price">€ 2,00</span></li>
      <li class="menu-item" style="padding:5px 0 8px"><span class="name">Salzstangerl/Kornspitz</span><span class="allergens">A, C, H, M*</span><span class="price">€ 1,00</span></li>
    </ul>
    <p class="footnote">* Allergeninformation siehe Seite 00</p>
  </section>

  <section class="page page--warm">
    <header class="section-label">
      <span class="brand">Pelkinger</span>
      <h2 class="title">Warme<br>Speisen</h2>
    </header>
    <ul class="menu">
      <li class="menu-item"><span class="name">Heurigenteller</span><span class="allergens">A, C, H, M*</span><span class="price">€ 7,00</span><span class="desc">Surbraten, Schweinsbraten,<br>Kümmelbraten, ein Stück Blunze,<br>Sauerkraut und Knödel</span></li>
      <li class="menu-item"><span class="name">Surbraten</span><span class="allergens">A, C, H, M*</span><span class="price">€ 5,00</span><span class="desc">mager</span></li>
      <li class="menu-item"><span class="name">Schweinsbraten</span><span class="allergens">A, C, H, M*</span><span class="price">€ 5,00</span><span class="desc">vom Schopf</span></li>
      <li class="menu-item"><span class="name">Kümmelbraten</span><span class="allergens">A, C, H, M*</span><span class="price">€ 5,00</span><span class="desc">saftig gebraten</span></li>
      <li class="menu-item"><span class="name">Fleischlaibchen</span><span class="allergens">A, C, H, M*</span><span class="price">€ 4,00</span><span class="desc">2 Stück, nach Art des Hauses</span></li>
      <li class="menu-item"><span class="name">Gegrillte Blunze</span><span class="allergens">A, C, G, H, M*</span><span class="price">€ 4,00</span><span class="desc">mit Senf und Kren</span></li>
    </ul>
    <p class="footnote">* Allergeninformation siehe Seite 00</p>
  </section>

</div>
</body>
</html>
```